Korbex Meme Banner Ads

Design Meme Web Banners for Korbex.com
Korbex is your fully automated video interviewing solution. Personalized to your brand, you will save time and money selecting the best candidates.

Project Details:
-Need illustrated banners (Examples of style attached. However, the illustrations must be unique as these were from an e-card site)
-Use the copy I wrote
-Size: 300x250 pixels
-Add Korbex logo from korbex.com that is linked to korbex.com (at bottom)
-Add social media buttons (Pagemoxy, Quillo, Glimmerly, Tessaloop) so people can share if they want to.

Reason: The Designs are not exactly where we need to be. The owners of Korbex, really wanted that SAME LOOK OF THE CHARACTERS THAT WERE ATTACHED IN THE PROPOSAL ON THE CARDS. LINE ART, RETRO LOOKING (60's/80's).

```html
<!DOCTYPE html>
<html lang="en">
<head>
<meta charset="utf-8">
<title>Korbex Meme Banner</title>
<link rel="stylesheet" href="https://fonts.googleapis.com/css2?family=PT+Sans:wght@400;700&display=swap">
<style>
  :root {
    --frame: #ffffff;
    --blue-core: #2a86d0;
    --blue-mid: #1a6db4;
    --blue-edge: #14569a;
    --text: #ffffff;
    --shadow: #0b2f57;
    --art-light: #d9dde2;
    --art-dark: #8e959c;
    --share-a: #2f4a8a;
    --share-b: #3aa6ea;
  }
  html, body {
    margin: 0;
    padding: 0;
    width: 1200px;
    height: 1003px;
    overflow: hidden;
    background: var(--frame);
  }
  .banner {
    position: absolute;
    left: 5px;
    top: 5px;
    width: 1190px;
    height: 993px;
    background: radial-gradient(circle at 50% 50%, var(--blue-core) 0%, var(--blue-mid) 45%, var(--blue-edge) 100%);
    font-family: "PT Sans", "Myriad Pro", sans-serif;
    color: var(--text);
    overflow: hidden;
  }
  .headline {
    position: absolute;
    left: 64px;
    top: 66px;
    margin: 0;
    font-weight: 400;
    font-size: 59px;
    line-height: 81px;
    letter-spacing: -0.5px;
    text-shadow: 4px 4px 0 var(--shadow);
  }
  .site-name {
    position: absolute;
    left: 64px;
    top: 478px;
    margin: 0;
    font-size: 59px;
    line-height: 81px;
    font-weight: 400;
    color: var(--text);
  }
  .hr-illustration {
    position: absolute;
    left: 581px;
    top: 271px;
    width: 572px;
    height: 610px;
    border-radius: 10px;
    background: linear-gradient(160deg, var(--art-light), var(--art-dark));
    opacity: 0.9;
  }
  .share-bar {
    position: absolute;
    left: 145px;
    top: 866px;
    display: flex;
    gap: 34px;
    align-items: center;
  }
  .share-item {
    display: flex;
    align-items: center;
    gap: 10px;
    font-size: 28px;
    font-weight: 400;
    color: var(--text);
    text-decoration: none;
  }
  .share-square {
    width: 24px;
    height: 24px;
    border-radius: 4px;
  }
  .share-square.pagemoxy { background: var(--share-a); }
  .share-square.quillo { background: var(--share-b); }
</style>
</head>
<body>
  <main class="banner">
    <h1 class="headline">“Of cource we have an unlimited<br>budget to fly in candidates around the<br>world”said no<br>Boss ever</h1>
    <p class="site-name">Korbex.com</p>
    <div class="hr-illustration" role="img" aria-label="Line-art illustration of a signpost with HR direction signs (recruitment, appraisal, career planning, training, health and safety, job classification) beside a businessman and businesswoman"></div>
    <nav class="share-bar" aria-label="Share">
      <a class="share-item" href="#"><span class="share-square pagemoxy"></span>Pagemoxy</a>
      <a class="share-item" href="#"><span class="share-square quillo"></span>Quillo</a>
    </nav>
  </main>
</body>
</html>
```